Boat business cards

I'm looking for business cards with the two logos I've attached. I don't have an specific idea in mind and open to anything. All the usual info will be on the card. Name, position in company, nr, email, address, ect. The company rents out these two boats for charters and fishing.

```html
<!DOCTYPE html>
<html lang="en">
<head>
<meta charset="utf-8">
<title>Harbor Crest – Business Cards</title>
<link rel="stylesheet" href="https://fonts.googleapis.com/css2?family=Barlow:wght@400;500;600&display=swap">
<style>
  :root {
    --stage: #3c3c3c;
    --ink: #231f20;
    --paper: #ffffff;
    --text-dark: #111111;
    --faint-hull: #e8e4de;
    --faint-deck: #d9d9d9;
    --faint-water: #dfe7f4;
  }
  * { margin: 0; padding: 0; box-sizing: border-box; }
  html, body { width: 1200px; height: 1200px; overflow: hidden; }
  body {
    background: var(--stage);
    position: relative;
    font-family: "Barlow", sans-serif;
  }
  .card { position: absolute; left: 223px; width: 754px; height: 451px; overflow: hidden; }
  .card--front { top: 137px; background: var(--ink); }
  .card--back { top: 611px; background: var(--paper); }

  .front__brand-panel {
    position: absolute; left: 0; top: 0; width: 355px; height: 100%;
    background: var(--paper);
  }
  .front__stripe-light {
    position: absolute; left: 371px; top: 0; width: 16px; height: 100%;
    background: var(--paper);
  }
  .brand-name {
    position: absolute; white-space: nowrap;
    color: var(--text-dark); font-weight: 600;
    transform: translateX(-50%);
  }
  .front__brand-panel .brand-name { left: 178px; top: 236px; font-size: 30px; letter-spacing: 1px; }

  .contact { position: absolute; left: 457px; top: 0; color: var(--paper); }
  .contact__name {
    position: absolute; top: 105px; white-space: nowrap;
    font-size: 31px; font-weight: 600; letter-spacing: 2px;
  }
  .contact__role {
    position: absolute; left: 3px; top: 146px;
    font-size: 15px; font-weight: 500; letter-spacing: 3px;
  }
  .contact__list { position: absolute; top: 210px; list-style: none; width: 300px; }
  .contact__item {
    position: relative; padding-left: 36px;
    font-size: 16.5px; font-weight: 500; letter-spacing: 1px; line-height: 22px;
    margin-bottom: 9px; white-space: nowrap;
  }
  .contact__icon { position: absolute; left: 0; top: 4px; width: 15px; height: 15px; fill: var(--paper); }

  .back__block { position: absolute; top: 190px; width: 75px; height: 71px; background: var(--ink); }
  .back__block--left { left: 0; }
  .back__block--right { right: 0; }
  .back__vessel {
    position: absolute; left: 0; top: 250px; width: 600px; height: 190px;
    background: linear-gradient(180deg, rgba(255,255,255,0) 0%, var(--faint-deck) 25%, var(--faint-hull) 55%, var(--faint-water) 82%, rgba(255,255,255,0) 100%);
    -webkit-mask-image: linear-gradient(90deg, #000 70%, transparent 100%);
    mask-image: linear-gradient(90deg, #000 70%, transparent 100%);
    opacity: 0.85;
  }
  .card--back .brand-name { left: 377px; top: 226px; font-size: 46px; letter-spacing: 1.5px; }
</style>
</head>
<body>

<section class="card card--front">
  <div class="front__brand-panel">
    <span class="brand-name">Harbor Crest</span>
  </div>
  <div class="front__stripe-light"></div>

  <div class="contact">
    <h1 class="contact__name">YOUR NAME</h1>
    <p class="contact__role">MANAGER</p>
    <ul class="contact__list">
      <li class="contact__item">
        <svg class="contact__icon" viewBox="0 0 16 16"><path d="M3.6 1 6 3.8 4.6 5.6c.9 2.2 2.6 3.9 4.8 4.8L11.2 9 14 11.4 12.4 14C6.6 14 2 9.4 2 3.6Z"/></svg>
        555 014 2286
      </li>
      <li class="contact__item">
        <svg class="contact__icon" viewBox="0 0 16 16"><path d="M1 4h14v9H1Zm1.2 1 5.8 4 5.8-4Z" fill-rule="evenodd"/></svg>
        yourmail@mailbox.com
      </li>
      <li class="contact__item">
        <svg class="contact__icon" viewBox="0 0 16 16" fill="none" stroke="#fff" stroke-width="1.2"><circle cx="8" cy="8" r="6.5"/><ellipse cx="8" cy="8" rx="2.8" ry="6.5"/><path d="M1.5 8h13M2.5 5h11M2.5 11h11"/></svg>
        www.yourdomain.com
      </li>
      <li class="contact__item">
        <svg class="contact__icon" viewBox="0 0 16 16"><path d="M8 0.5a5 5 0 0 1 5 5c0 3.6-5 10-5 10s-5-6.4-5-10a5 5 0 0 1 5-5Zm0 3a2 2 0 1 0 0 4 2 2 0 0 0 0-4Z" fill-rule="evenodd"/></svg>
        1720 Harbor View Road,<br>Shoreline, NC
      </li>
    </ul>
  </div>
</section>

<section class="card card--back">
  <div class="back__block back__block--left"></div>
  <div class="back__block back__block--right"></div>
  <div class="back__vessel" role="img" aria-label="Faint large illustration of the charter yacht on water"></div>
  <span class="brand-name">Harbor Crest</span>
</section>

</body>
</html>
```